Manufacturers Catalog Cover Page

We are looking to have a cover to our catalog page designed. I currently have begun work for the remained of the catalog in InDesign and want the cover created in InDesign. I will provide photos.

Looking to beable to add the cover to our existing attached catalog.

Industry/Entity Type

Manufacturing

Requirements
Must have
• Colors match what we are currently using. The Dark grey and gold
Nice to have
• modern, clean

```html
<!DOCTYPE html>
<html lang="en">
<head>
<meta charset="utf-8">
<title>Summit Elastomers — Catalog Cover</title>
<link rel="stylesheet" href="https://fonts.googleapis.com/css2?family=Bebas+Neue&display=swap">
<style>
  :root{
    --stage:#d3d4d6;
    --charcoal:#3a3a3a;
    --gold:#d7c39c;
    --gold-deep:#c4a46b;
    --gold-dark:#a2854f;
    --ink:#2b2b2b;
    --white:#f4f1ea;
  }
  *{margin:0;padding:0;box-sizing:border-box}
  html,body{width:930px;height:1200px;overflow:hidden;background:var(--stage)}
  body{position:relative;font-family:"Bebas Neue",Impact,sans-serif}
  .defs{position:absolute;width:0;height:0}
  .panel{position:absolute;width:408px;height:530px;background:var(--charcoal);overflow:hidden}
  .front-cover{left:302px;top:46px}
  .spread{position:absolute;left:58px;top:630px;width:816px;height:530px}
  .spread .back{left:0;top:0}
  .spread .front{left:408px;top:0}
  .panel-art{position:absolute;inset:0;width:408px;height:530px}
  .kicker{position:absolute;left:44px;top:44px;color:var(--white);font-size:21px;line-height:19px;letter-spacing:.2px}
  .rule{position:absolute;left:44px;top:102px;width:30px;height:1px;background:var(--gold-dark)}
  .headline{position:absolute;left:44px;top:112px;color:var(--gold);font-size:32px;line-height:29px}
  .brand{position:absolute;display:flex;align-items:center;gap:9px}
  .brand-dot{width:50px;height:50px;border-radius:50%;background:var(--gold);flex:none}
  .brand-name{color:var(--white);font-size:20px;line-height:18px}
  .front .brand,.front-cover .brand{left:222px;top:38px}
  .back .brand{left:40px;top:32px}
  .phones{position:absolute;left:97px;top:96px;color:var(--white);font-size:17px;line-height:16px}
  .web-small{position:absolute;left:97px;top:139px;color:var(--gold);font-size:9px;letter-spacing:.2px}
  .sector{position:absolute;width:76px;height:76px;border-radius:50%;border:1.5px solid rgba(255,255,255,.85)}
  .footer-bar{position:absolute;left:0;top:482px;width:408px;height:32px;background:var(--gold);color:var(--ink);font-size:16px;display:flex;align-items:center;justify-content:center;letter-spacing:.3px}
</style>
</head>
<body>
<svg class="defs" aria-hidden="true">
  <defs>
    <linearGradient id="stockGrad" x1="0" y1="0" x2="1" y2="1">
      <stop offset="0" stop-color="#6d6e70"/>
      <stop offset=".45" stop-color="#3f4042"/>
      <stop offset=".7" stop-color="#8a5036"/>
      <stop offset="1" stop-color="#2a2b2d"/>
    </linearGradient>
    <linearGradient id="coilGrad" x1="0" y1="0" x2="1" y2="1">
      <stop offset="0" stop-color="#7a7b7d"/>
      <stop offset=".5" stop-color="#45464a"/>
      <stop offset="1" stop-color="#2b2c2e"/>
    </linearGradient>
  </defs>
</svg>

<!-- Single front cover -->
<section class="panel front-cover">
  <svg class="panel-art" viewBox="0 0 408 530">
    <path role="img" aria-label="Photo of coiled rubber and plastic extrusion profiles" fill="url(#stockGrad)" d="M0 292 C150 272 300 200 408 120 L408 530 L0 530 Z"/>
    <path fill="var(--gold-dark)" d="M0 236 C150 228 300 152 408 78 L408 96 C300 168 150 244 0 252 Z"/>
    <path fill="var(--gold)" d="M0 256 C150 248 300 172 408 100 L408 124 C300 196 150 272 0 282 Z"/>
  </svg>
  <p class="kicker">Rubber &amp;<br>Plastic Extursion</p>
  <span class="rule"></span>
  <h1 class="headline">Gaskets,<br>Trims &amp; Seals</h1>
  <div class="brand"><span class="brand-dot"></span><span class="brand-name">Summit<br>Elastomers</span></div>
  <div class="sector" role="img" aria-label="Photo of an automated robotic production line" style="left:35px;top:204px;background:linear-gradient(180deg,#b9c9dc,#d9c043 70%,#6f7680)"></div>
  <div class="sector" role="img" aria-label="Photo of a combine harvester in a field" style="left:128px;top:200px;background:linear-gradient(180deg,#7fb0df,#e8eef3 45%,#d9a41c 70%,#6b5a2a)"></div>
  <div class="sector" role="img" aria-label="Photo of a backhoe loader on a site" style="left:218px;top:174px;background:linear-gradient(180deg,#4f8fd6,#a9cbea 45%,#e09a21 70%,#4c4331)"></div>
  <div class="sector" role="img" aria-label="Photo of a modern glass office building" style="left:305px;top:138px;background:linear-gradient(180deg,#8fb7e3,#c8d5df 50%,#7f94a6 80%,#6f8a5a)"></div>
  <div class="footer-bar">www.summitelastomers.com</div>
</section>

<!-- Open spread: back and front -->
<div class="spread">
  <section class="panel back">
    <svg class="panel-art" viewBox="0 0 408 530">
      <path role="img" aria-label="Photo of coiled black and grey rubber extrusions" fill="url(#coilGrad)" d="M0 205 C120 230 250 270 408 290 L408 530 L0 530 Z"/>
      <path fill="var(--gold)" d="M0 165 C120 192 250 240 408 268 L408 286 C250 262 120 222 0 194 Z"/>
    </svg>
    <div class="brand"><span class="brand-dot"></span><span class="brand-name">Summit<br>Elastomers</span></div>
    <p class="phones">888-555-0142<br>330-555-0187</p>
    <p class="web-small">www.summitelastomers.com</p>
    <div class="sector" role="img" aria-label="Photo of rolled rubber seal strips" style="left:21px;top:153px;background:linear-gradient(135deg,#f2f2f2,#b0262a 45%,#2a2a2a 70%,#c8a574)"></div>
    <div class="sector" role="img" aria-label="Photo of a speedboat on open water" style="left:110px;top:184px;background:linear-gradient(180deg,#c9dced,#f0f0f0 45%,#2f6c9c 65%,#1f4a6e)"></div>
    <div class="sector" role="img" aria-label="Photo of black rubber seal profiles" style="left:204px;top:210px;background:linear-gradient(135deg,#f4f1f4,#3a3336 45%,#1c1a1c 70%,#e6e0e6)"></div>
    <div class="sector" role="img" aria-label="Photo of a motorhome on a desert road" style="left:296px;top:221px;background:linear-gradient(180deg,#9cc2e6,#c98a5c 40%,#3a3a3a 70%,#8a6a4e)"></div>
    <div class="footer-bar">www.summitelastomers.com</div>
  </section>

  <section class="panel front">
    <svg class="panel-art" viewBox="0 0 408 530">
      <path role="img" aria-label="Photo of coiled rubber and plastic extrusion profiles" fill="url(#stockGrad)" d="M0 292 C150 272 300 200 408 120 L408 530 L0 530 Z"/>
      <path fill="var(--gold-dark)" d="M0 236 C150 228 300 152 408 78 L408 96 C300 168 150 244 0 252 Z"/>
      <path fill="var(--gold)" d="M0 256 C150 248 300 172 408 100 L408 124 C300 196 150 272 0 282 Z"/>
    </svg>
    <p class="kicker">Rubber &amp;<br>Plastic Extursion</p>
    <span class="rule"></span>
    <h2 class="headline">Gaskets,<br>Trims &amp; Seals</h2>
    <div class="brand"><span class="brand-dot"></span><span class="brand-name">Summit<br>Elastomers</span></div>
    <div class="sector" role="img" aria-label="Photo of an automated robotic production line" style="left:35px;top:204px;background:linear-gradient(180deg,#b9c9dc,#d9c043 70%,#6f7680)"></div>
    <div class="sector" role="img" aria-label="Photo of a combine harvester in a field" style="left:128px;top:200px;background:linear-gradient(180deg,#7fb0df,#e8eef3 45%,#d9a41c 70%,#6b5a2a)"></div>
    <div class="sector" role="img" aria-label="Photo of a backhoe loader on a site" style="left:218px;top:174px;background:linear-gradient(180deg,#4f8fd6,#a9cbea 45%,#e09a21 70%,#4c4331)"></div>
    <div class="sector" role="img" aria-label="Photo of a modern glass office building" style="left:305px;top:138px;background:linear-gradient(180deg,#8fb7e3,#c8d5df 50%,#7f94a6 80%,#6f8a5a)"></div>
    <div class="footer-bar">www.summitelastomers.com</div>
  </section>
</div>
</body>
</html>
```